business card design and proof

business card design
- logos attached
- black and white only
-minimal design/ clean design
-logo on front and information on the back
-information provided in document attached - tittle - Logistics Event Director
social media handle icons - Facebook, Instagram, pinterest

```html
<!DOCTYPE html>
<html lang="en">
<head>
<meta charset="utf-8">
<title>Cityline Gatherings — Business Card</title>
<link rel="stylesheet" href="https://fonts.googleapis.com/css2?family=Oswald:wght@600&family=Roboto:wght@400;700&display=swap">
<style>
  :root {
    --stage: #2b2b2b;
    --card-dark: #2a2123;
    --card-light: #ffffff;
    --ink: #1a1a1a;
    --ink-soft: #555555;
    --rule: #9a9a9a;
    --on-dark: #ffffff;
  }
  * { box-sizing: border-box; margin: 0; padding: 0; }
  html, body { width: 1200px; height: 900px; overflow: hidden; }
  body {
    background: var(--stage);
    display: flex;
    flex-direction: column;
    align-items: center;
    justify-content: center;
    gap: 44px;
    font-family: "Roboto", Arial, sans-serif;
  }
  .card {
    width: 660px;
    height: 377px;
    position: relative;
    overflow: hidden;
    box-shadow: 0 14px 30px rgba(0,0,0,0.45);
  }

  /* Front */
  .card--front {
    background: var(--card-dark);
    display: flex;
    flex-direction: column;
    align-items: center;
    justify-content: center;
    gap: 26px;
  }
  .brand {
    display: flex;
    align-items: center;
    gap: 14px;
    font-family: "Oswald", "Arial Narrow", sans-serif;
    font-weight: 600;
    letter-spacing: 2px;
    text-transform: uppercase;
  }
  .brand__mark { width: 16px; height: 16px; border-radius: 50%; }
  .card--front .brand { color: var(--on-dark); font-size: 40px; }
  .card--front .brand__mark { background: var(--on-dark); }
  .social { display: flex; gap: 12px; }
  .social__dot { width: 12px; height: 12px; border-radius: 50%; background: var(--on-dark); }

  /* Back */
  .card--back { background: var(--card-light); }
  .card__divider { position: absolute; inset: 0; }
  .contact {
    position: absolute;
    left: 40px;
    top: 148px;
    color: var(--ink);
  }
  .contact__name { font-weight: 700; font-size: 19px; letter-spacing: 0.5px; }
  .contact__title {
    font-size: 14px;
    color: var(--ink-soft);
    letter-spacing: 0.5px;
    padding-bottom: 6px;
    border-bottom: 1.5px solid var(--rule);
    margin-bottom: 16px;
    display: inline-block;
  }
  .contact__list { list-style: none; display: flex; flex-direction: column; gap: 9px; }
  .contact__item { display: flex; align-items: center; gap: 10px; font-size: 14.5px; }
  .contact__icon {
    width: 22px; height: 22px;
    background: var(--ink);
    border-radius: 3px;
    display: flex; align-items: center; justify-content: center;
  }
  .card--back .brand {
    position: absolute;
    right: 38px;
    top: 166px;
    color: var(--ink);
    font-size: 26px;
  }
  .card--back .brand__mark { width: 12px; height: 12px; background: var(--ink); }
</style>
</head>
<body>
  <section class="card card--front" aria-label="Card front">
    <div class="brand"><span class="brand__mark"></span><span>Cityline Gatherings</span></div>
    <div class="social" aria-label="Social media">
      <span class="social__dot"></span><span class="social__dot"></span><span class="social__dot"></span>
    </div>
  </section>

  <section class="card card--back" aria-label="Card back">
    <svg class="card__divider" width="660" height="377" viewBox="0 0 660 377" aria-hidden="true">
      <polygon points="330,0 660,0 660,377 395,377" fill="#f6f6f6"/>
      <line x1="330" y1="0" x2="395" y2="377" stroke="#e4e4e4" stroke-width="1.5"/>
    </svg>
    <div class="contact">
      <p class="contact__name">CLARA WHITFIELD</p>
      <p class="contact__title">LOGISTICS EVENT COORDINATOR</p>
      <ul class="contact__list">
        <li class="contact__item">
          <span class="contact__icon"><svg width="14" height="14" viewBox="0 0 24 24"><path d="M6.6 10.8a15 15 0 0 0 6.6 6.6l2.2-2.2c.3-.3.7-.4 1-.2 1.1.4 2.3.6 3.6.6.6 0 1 .4 1 1V20c0 .6-.4 1-1 1C10.6 21 3 13.4 3 4c0-.6.4-1 1-1h3.5c.6 0 1 .4 1 1 0 1.3.2 2.5.6 3.6.1.3 0 .7-.2 1z" fill="#fff"/></svg></span>
          <span>555 014 2290</span>
        </li>
        <li class="contact__item">
          <span class="contact__icon"><svg width="14" height="14" viewBox="0 0 24 24"><rect x="3" y="5" width="18" height="14" rx="1" fill="none" stroke="#fff" stroke-width="2"/><path d="M3 6l9 7 9-7" fill="none" stroke="#fff" stroke-width="2"/></svg></span>
          <span>hello@citylinegatherings.com</span>
        </li>
        <li class="contact__item">
          <span class="contact__icon"><svg width="14" height="14" viewBox="0 0 24 24"><circle cx="12" cy="12" r="9" fill="none" stroke="#fff" stroke-width="2"/><path d="M3 12h18M12 3c3 3 3 15 0 18M12 3c-3 3-3 15 0 18" fill="none" stroke="#fff" stroke-width="1.6"/></svg></span>
          <span>www.citylinegatherings.com</span>
        </li>
      </ul>
    </div>
    <div class="brand"><span class="brand__mark"></span><span>Cityline Gatherings</span></div>
  </section>
</body>
</html>
```